Luxury Court Grove/academy - Webdesign

We want to develop a cutting edge website for a luxury tennis academy. Academy is based in Russia and includes all the necessary amenities for comfortable stay: apartments, spa, tennis courts, training facilities, etc.
We would like to see a clean, simple and modern design (with implementation of all the current trends in web design, although our project has to be distinct and unique).
Color scheme: we would like to see colors present in our logos and all the current associated with tennis. We are open to your ideas and creativity on this front.
The final design should communicate simplicity, be user friendly and convey premium feel.
We woud like to see unique ideas in the design, unconventional techniques, etc.
We don't want standard template design!
Updates
We want to mention that this Tennis Academy has a light focus on nature, as the new material we have uploaded illustrates.
Additional comment to everyone!
We couldn't upload this file to the system: it is too big.
Thank you everyone for your submissions!
Industry/Entity Type
Training
Requirements
Must have
- We would like to see the designs for the following pages:
Home Page:
- Slideshow
- Short description and all the standard stuff
About Us:
- Description with some images
Services:
- Simple description of all of the provided services and possibility to book all of them on the website
! Important ! Develop small system for booking of the days of stay and registration for the courses
Booking and registration !
News:
- Creative layout to display recent news of the academy
Coaches:
- Image and short description of our staff.
Club / Gallery:
- Images and descriptions of the amenities in the territory.
We want a unique display of images: not just lines and rows filled with images
- One idea: an interactive map that displays images and description on mouseover or click on the object on the map (but again, we are open to all your ideas)
Contacts:
- Contact form, contacts, etc.
Sport Store:
- Basic layout for the goods and services provided by the sports store located in the academy
Prices:
- Price lists and ranges with a button leading to registration and booking
For pages like About Us and Services, it would be enough to develop one unified layout for all of them.

```html
<!DOCTYPE html>
<html lang="en">
<head>
<meta charset="utf-8">
<title>Court Grove – Home</title>
<link href="https://fonts.googleapis.com/css2?family=Roboto+Condensed:wght@400;700&family=Arimo:wght@400;700&display=swap" rel="stylesheet">
<style>
:root{
  --bg:#f1f1f0;
  --ink:#8c8c8c;
  --ink-soft:#a3a3a3;
  --heading:#7d7d7d;
  --green-dark:#0d4a2b;
  --green-nav:#0f5230;
  --green:#5c9a36;
  --green-link:#1b6a34;
  --lime:#a9cf3b;
  --lime-light:#c3e15a;
  --footer:#2b5f35;
  --white:#ffffff;
}
*{box-sizing:border-box;margin:0;padding:0}
html,body{width:1187px;height:1200px;overflow:hidden;background:var(--bg)}
body{font-family:"Arimo",Arial,sans-serif;color:var(--ink)}
.page{position:relative;width:1187px;height:1200px;background:
  repeating-linear-gradient(0deg,rgba(0,0,0,.012) 0 1px,transparent 1px 3px),var(--bg)}
.abs{position:absolute}
.cond{font-family:"Roboto Condensed","Arial Narrow",sans-serif}

/* header */
.brand{left:111px;top:30px;display:flex;align-items:center;gap:10px;font-family:"Roboto Condensed",sans-serif;font-weight:700;font-size:40px;color:var(--green-link);letter-spacing:.5px}
.brand-dot{width:30px;height:30px;border-radius:50%;background:var(--lime)}
.top-links{right:112px;top:16px;display:flex;gap:11px;font-family:"Roboto Condensed",sans-serif;font-weight:700;font-size:14px;letter-spacing:.6px;color:var(--green-link)}
.top-links .active{color:var(--lime)}
.top-links .sep{color:var(--green-link);font-weight:400}
.btn{top:51px;height:38px;border-radius:6px;border:3px solid var(--lime-light);background:linear-gradient(#b5d84a,#92c02b);color:var(--white);font-family:"Roboto Condensed",sans-serif;font-weight:700;font-size:14px;letter-spacing:.5px;display:flex;align-items:center;justify-content:center;box-shadow:0 4px 6px rgba(0,0,0,.08)}
.btn-book{left:744px;width:237px}
.btn-search{left:995px;width:80px}

/* main nav */
.main-nav{left:152px;top:144px;width:882px;height:59px;border-radius:7px;border:3px solid #1a8a43;background:linear-gradient(#0e5532,var(--green-dark));box-shadow:0 10px 12px -6px rgba(0,0,0,.35);display:flex;align-items:stretch;padding-left:33px}
.main-nav a{display:flex;align-items:center;padding:0 22px;color:#e8efe9;text-decoration:none;font-family:"Roboto Condensed",sans-serif;font-weight:700;font-size:19px;letter-spacing:1px;margin-right:2px}
.main-nav a.current{background:var(--lime);color:var(--green-dark);padding:0 11px;margin-right:13px}

/* welcome */
.section-title{font-family:"Roboto Condensed",sans-serif;font-size:18px;letter-spacing:1px;display:flex;align-items:center;gap:8px}
.section-title::after{content:"";flex:1;height:8px;background:repeating-linear-gradient(90deg,#d2d2d2 0 1px,transparent 1px 2px),repeating-linear-gradient(0deg,#d2d2d2 0 1px,transparent 1px 2px);opacity:.6}
.welcome-title{left:116px;top:231px;width:441px;color:var(--heading)}
.welcome-text{left:121px;top:266px;width:436px;font-size:12.4px;line-height:17.8px;text-align:justify}
.welcome-text p{margin-bottom:6px}
.hero-frame{left:575px;top:233px;width:486px;height:332px;border:1px dotted #9a9a9a;padding:5px;background:#fff;box-shadow:0 14px 14px -10px rgba(0,0,0,.25)}
.hero-photo{width:100%;height:100%;background:linear-gradient(160deg,#8fae5c 0%,#c98a5b 55%,#a6533a 85%,#3b3b3b 100%)}

/* gallery */
.gallery{left:111px;top:609px;width:964px;height:249px;background:#fafafa;border:1px solid #dcdcdc;box-shadow:0 0 0 4px #fff inset,0 0 0 5px #e2e2e2 inset}
.tile{top:20px;width:193px}
.tile-title{color:var(--green);font-size:14px;font-weight:700;letter-spacing:.8px;display:flex;align-items:center;gap:8px}
.tile-title::before,.tile-title::after{content:"";flex:1;height:4px;border-top:1px dotted #cfcfcf;border-bottom:1px dotted #cfcfcf}
.tile-photo{margin-top:9px;border:1px dotted #cfcfcf;padding:3px;background:#fff}
.tile-photo div{height:185px;background:linear-gradient(165deg,#d9a37c 0%,#e9c09c 45%,#f3e3cf 100%)}

/* lower columns */
.col{top:884px;width:260px}
.col .section-title{color:var(--green);font-size:17px}
.col ul{list-style:none;margin-top:20px}
.col li{position:relative;padding-left:26px;font-size:12.4px;line-height:18px;color:var(--ink-soft);text-align:justify;margin-bottom:14px}
.col li::before{content:"";position:absolute;left:6px;top:4px;border-left:7px solid #9a9a9a;border-top:5px solid transparent;border-bottom:5px solid transparent}
.blog-item{display:flex;gap:9px;margin-top:20px;font-size:12.4px;line-height:18px;color:var(--ink-soft)}
.blog-item + .blog-item{margin-top:14px}
.date{flex:none;width:45px;height:45px;border-radius:5px;background:linear-gradient(#c4c4c4,#a6a6a6);border:2px solid #e2e2e2;color:#fff;font-family:"Roboto Condensed",sans-serif;font-size:11px;text-align:center;line-height:18px;padding-top:3px}
.blog-item p{text-align:justify}
.blog-item .by{display:block;text-align:right}

/* footer */
.footer{left:0;top:1080px;width:1187px;height:120px;background:var(--footer)}
.footer-badge{left:150px;top:12px;width:104px;height:75px;background:#fff;border-radius:6px;box-shadow:0 2px 6px rgba(0,0,0,.4);display:flex;align-items:center;justify-content:center;font-family:"Roboto Condensed",sans-serif;font-weight:700;font-size:18px;color:#555}
.copyright{left:115px;top:100px;font-size:10px;color:#e3ece3}
.newsletter-title{left:708px;top:21px;color:#fff;font-size:18px;font-weight:700;letter-spacing:.5px}
.email{left:709px;top:41px;width:237px;height:30px;border-radius:5px;background:#0c3a1e;border:2px solid #1d5f33;color:#dfe8df;font-size:10.5px;display:flex;align-items:center;padding-left:9px}
.subscribe{left:953px;top:41px;width:82px;height:30px;border-radius:5px;background:#0c2e1a;border:2px solid #3b7a4a;color:#fff;font-family:"Roboto Condensed",sans-serif;font-weight:700;font-size:14px;display:flex;align-items:center;justify-content:center}
.footer-links{right:112px;top:91px;display:flex;gap:10px;font-size:10.5px;color:#fff}
</style>
</head>
<body>
<div class="page">

  <header>
    <div class="abs brand"><span>Court Grove</span><span class="brand-dot"></span></div>
    <nav class="abs top-links">
      <span class="active">HOME</span><span class="sep">I</span>
      <span>ABOUT US</span><span class="sep">I</span>
      <span>GALLERY</span><span class="sep">I</span>
      <span>CONTACT US</span>
    </nav>
    <div class="abs btn btn-book">FREE REGISTRATION AND BOOKING</div>
    <div class="abs btn btn-search">SEARCH</div>
    <nav class="abs main-nav">
      <a class="current">HOME</a>
      <a>APARTMENTS</a>
      <a>SPA</a>
      <a>TENNIS COURTS</a>
      <a>TRAINING FACILITIES</a>
      <a>OUR STAFF</a>
    </nav>
  </header>

  <section>
    <h2 class="abs section-title welcome-title">WELCOME TO OUR SITE</h2>
    <div class="abs welcome-text">
      <p>Lorem ipsum dolor sit amet, consectetur adipiscing elit. In pellentesque dolor quis neque viverra rhoncus a vel lorem. Pellentesque habitant morbi tristique senectus et netus et malesuada fames ac turpis egestas. Vivamus sit amet turpis at purus fringilla malesuada. Pellentesque in ante metus, a luctus dolor. Donec non pulvinar purus. Praesent dapibus molestie erat et lobortis. Nullam pretium sagittis velit a vehicula. Donec consequat nibh ac dolor rutrum elementum gravida felis congue. Integer erat metus, tempor sed dapibus ac, semper et lectus. Sed a nibh velit, ut posuere mauris.</p>
      <p>Lorem ipsum dolor sit amet, consectetur adipiscing elit. In pellentesque dolor quis neque viverra rhoncus a vel lorem. Pellentesque habitant morbi tristique senectus et netus et malesuada fames ac turpis egestas. Vivamus sit amet turpis at purus fringilla malesuada. Pellentesque in ante metus, a luctus dolor. Donec non pulvinar purus. Praesent dapibus molestie erat et lobortis. Nullam pretium sagittis velit a vehicula. Donec consequat nibh ac dolor rutrum elementum gravida felis congue. Integer erat metus, tempor sed dapibus ac, semper et lectus. Sed a nibh velit, ut posuere mauris.</p>
    </div>
    <div class="abs hero-frame"><div class="hero-photo" role="img" aria-label="Family with tennis rackets smiling behind the net on a clay court"></div></div>
  </section>

  <section class="abs gallery">
    <div class="abs tile cond" style="left:35px"><h3 class="tile-title">LOREM IPSUM</h3><div class="tile-photo"><div role="img" aria-label="Guest relaxing during a spa massage with candles"></div></div></div>
    <div class="abs tile cond" style="left:271px"><h3 class="tile-title">LOREM IPSUM</h3><div class="tile-photo"><div role="img" aria-label="Guest relaxing during a spa massage with candles"></div></div></div>
    <div class="abs tile cond" style="left:507px"><h3 class="tile-title">LOREM IPSUM</h3><div class="tile-photo"><div role="img" aria-label="Guest relaxing during a spa massage with candles"></div></div></div>
    <div class="abs tile cond" style="left:743px"><h3 class="tile-title">LOREM IPSUM</h3><div class="tile-photo"><div role="img" aria-label="Guest relaxing during a spa massage with candles"></div></div></div>
  </section>

  <section class="abs col" style="left:116px">
    <h2 class="section-title">LATEST NEWS</h2>
    <ul>
      <li>Lorem ipsum dolor sit amet, consectetur adipiscing elit. In pellentesque dolor</li>
      <li>Lorem ipsum dolor sit amet, consectetur adipiscing elit. In pellentesque dolor</li>
      <li>Lorem ipsum dolor sit amet, consectetur adipiscing elit. In pellentesque dolor</li>
    </ul>
  </section>

  <section class="abs col" style="left:465px">
    <h2 class="section-title">LATEST TWEETS</h2>
    <ul>
      <li>Lorem ipsum dolor sit amet, consectetur adipiscing elit. In pellentesque dolor</li>
      <li>Lorem ipsum dolor sit amet, consectetur adipiscing elit. In pellentesque dolor</li>
      <li>Lorem ipsum dolor sit amet, consectetur adipiscing elit. In pellentesque dolor</li>
    </ul>
  </section>

  <section class="abs col" style="left:822px;width:253px">
    <h2 class="section-title">LATEST ON THE BLOG</h2>
    <div class="blog-item"><div class="date">27 JAN<br>2012</div><p>Lorem ipsum dolor sit amet, consectetur adipiscing elit. In <span class="by">- Lorem ipsum</span></p></div>
    <div class="blog-item"><div class="date">27 JAN<br>2012</div><p>Lorem ipsum dolor sit amet, consectetur adipiscing elit. In <span class="by">- Lorem ipsum</span></p></div>
  </section>

  <footer class="abs footer">
    <div class="abs footer-badge">Court Grove</div>
    <div class="abs copyright">All Rights Reserved @ Court Grove</div>
    <h2 class="abs newsletter-title cond">NEWSLETTER</h2>
    <div class="abs email">ENTER YOUR EMAIL</div>
    <div class="abs subscribe">SUBSCRIBE</div>
    <nav class="abs footer-links">
      <span>HOME</span><span>|</span><span>ABOUT US</span><span>|</span><span>CONTACT US</span><span>|</span><span>PRIVACY POLICY</span><span>|</span><span>TERMS</span>
    </nav>
  </footer>

</div>
</body>
</html>
```